KBMR new business card design

We need a business card design for our established business which is Australia wide however based in Melbourne. We are a young team of Financial Planners who specialize in Insurance and Basic super advice for people like us.

We are people who help our clients get things done in a timely and cost effective manner whilst having a good time and a laugh along the way.

We would like this to have a consistent feel with our new e-brochure which i have attached from a color and font perspective.

Industry/Entity Type

Business

Requirements
Must have
• We do not need specific address details rather just the states we are in:

VIC/NSW/QLD/TAS
Nice to have
• Curved edge to mate the brochure

```html
<!DOCTYPE html>
<html lang="en">
<head>
<meta charset="utf-8">
<title>KBMR Business Card</title>
<link rel="stylesheet" href="https://fonts.googleapis.com/css2?family=Roboto:wght@400;500&family=Roboto+Condensed:wght@400&display=swap">
<style>
  :root {
    --page: #ffffff;
    --card-dark: #1c1c1c;
    --brand-green: #16a24b;
    --lime: #8cc24a;
    --contact-green: #8cc84b;
    --ink: #111111;
  }
  html, body {
    margin: 0;
    padding: 0;
    width: 1200px;
    height: 900px;
    overflow: hidden;
    background: var(--page);
  }
  .canvas {
    position: relative;
    width: 1200px;
    height: 900px;
  }
  .card {
    position: absolute;
    left: 74px;
    top: 126px;
    width: 1052px;
    height: 648px;
    overflow: hidden;
  }
  .card-art {
    position: absolute;
    inset: 0;
  }
  .web-address {
    position: absolute;
    left: 126px;
    top: 324px;
    transform: translate(-50%, -50%) rotate(-90deg);
    margin: 0;
    font-family: "Roboto", Arial, sans-serif;
    font-weight: 400;
    font-size: 60px;
    letter-spacing: 1px;
    color: var(--ink);
    white-space: nowrap;
  }
  .contact-list {
    position: absolute;
    left: 448px;
    top: 222px;
    margin: 0;
    padding: 0;
    list-style: none;
    font-family: "Roboto Condensed", "Arial Narrow", sans-serif;
    font-size: 25px;
    color: var(--contact-green);
  }
  .contact-item {
    display: flex;
    align-items: center;
    height: 43.5px;
  }
  .contact-icon {
    width: 28px;
    height: 28px;
    margin-right: 10px;
    flex: none;
  }
  .contact-item--regions {
    padding-left: 38px;
    letter-spacing: 1px;
    word-spacing: 4px;
  }
</style>
</head>
<body>
<main class="canvas">
  <section class="card" aria-label="KBMR business card">
    <svg class="card-art" width="1052" height="648" viewBox="0 0 1052 648" xmlns="http://www.w3.org/2000/svg">
      <defs>
        <radialGradient id="texture-tone" cx="55%" cy="45%" r="75%">
          <stop offset="0" stop-color="#262626"/>
          <stop offset="1" stop-color="#161616"/>
        </radialGradient>
        <filter id="soft-shade" x="-20%" y="-10%" width="140%" height="120%">
          <feDropShadow dx="0" dy="0" stdDeviation="6" flood-color="#000" flood-opacity="0.8"/>
        </filter>
      </defs>
      <rect class="mesh-background" role="img" aria-label="Dark hexagonal mesh texture" x="0" y="0" width="1052" height="648" fill="url(#texture-tone)"/>
      <path class="side-band" d="M0 0 H216 V246 L270 314 L216 382 V648 H0 Z" fill="var(--brand-green)"/>
      <path class="accent-bar" filter="url(#soft-shade)"
            d="M396 100 Q346 100 346 150 V558 H414 V100 Z"
            fill="var(--lime)"/>
    </svg>

    <p class="web-address">www.kbmr.com.au</p>

    <ul class="contact-list">
      <li class="contact-item">
        <svg class="contact-icon" viewBox="0 0 24 24" aria-hidden="true">
          <path d="M3 9 Q12 3 21 9 L19 12 L15 10 V8 H9 V10 L5 12 Z" fill="var(--brand-green)"/>
          <path d="M7 13 H17 L19 20 H5 Z" fill="var(--brand-green)"/>
          <circle cx="12" cy="16.5" r="2" fill="var(--card-dark)"/>
        </svg>
        <span>Phone: 1300 555 214</span>
      </li>
      <li class="contact-item">
        <svg class="contact-icon" viewBox="0 0 24 24" aria-hidden="true">
          <rect x="6" y="3" width="12" height="7" fill="var(--brand-green)"/>
          <rect x="3" y="10" width="18" height="10" rx="2" fill="var(--brand-green)"/>
          <rect x="7" y="13" width="10" height="2" fill="var(--card-dark)"/>
        </svg>
        <span>Fax: 03 9555 0147</span>
      </li>
      <li class="contact-item">
        <svg class="contact-icon" viewBox="0 0 24 24" aria-hidden="true">
          <rect x="7" y="2" width="10" height="20" rx="2" fill="var(--brand-green)"/>
          <rect x="9" y="5" width="6" height="12" fill="var(--card-dark)"/>
        </svg>
        <span>Mobile: 0400 555 872</span>
      </li>
      <li class="contact-item">
        <svg class="contact-icon" viewBox="0 0 24 24" aria-hidden="true">
          <rect x="3" y="6" width="18" height="13" fill="var(--brand-green)"/>
          <path d="M3 6 L12 13 L21 6" fill="none" stroke="var(--card-dark)" stroke-width="1.5"/>
        </svg>
        <span>sam@kbmr.com.au</span>
      </li>
      <li class="contact-item contact-item--regions">NSW, VIC, TAS, QLD.</li>
    </ul>
  </section>
</main>
</body>
</html>
```